Bold Website Redesign for a Disruptive Training Brand

Corvane Labs is a bold, no-fluff sales & leadership training company powered by AI-driven practice and behavioral science. We’ve already built our website structure and copy in Lovable.ai — now we need a designer to fully transform the visual design across all pages (Home, Approach, Programs, About, Contact).
We’re looking for a modern, memorable, high-performance aesthetic that blends human energy, science, and tech without feeling corporate or safe. Clean, bold typography, fluid layout, strong emotional hero moments, subtle motion, and imagery that mixes real people with abstract scientific/tech visuals.Because our clients are primarily North American, please ensure any human photography or AI-generated imagery reflects a North American business context and demographics (modern, diverse, and realistic).

Your job is visual redesign only — no coding required.
The final design must be practical to rebuild inside Lovable.ai.

A full, detailed creative brief (plus logo files) is included in the uploaded files.
If you can bring a mix of edge, intelligence, and strong visual storytelling, we’d love to see your work.

Website is already built in Lovable.ai at - https://corvane-website-tempdesign.plinkora-sites.app — structure is set, visuals need redesign.

Sick

```html
<!DOCTYPE html>
<html lang="en">
<head>
<meta charset="utf-8">
<title>Corvane Labs — Training That Practices Back</title>
<link href="https://fonts.googleapis.com/css2?family=Rubik:wght@500;600;700&family=Inter:wght@400;500;600;700&display=swap" rel="stylesheet">
<style>
:root{
  --blue:#0a4cf5;
  --cyan:#10d8ff;
  --cyan-soft:#a6ecff;
  --navy:#0b1a3c;
  --navy-foot:#0d2147;
  --navy-bar:#1b335e;
  --ink:#0e1a33;
  --text:#4a5568;
  --white:#ffffff;
  --head:"Rubik",sans-serif;
  --body:"Inter",sans-serif;
}
*{margin:0;padding:0;box-sizing:border-box}
html,body{width:1200px;height:3863px;overflow:hidden}
body{position:relative;background:var(--white);font-family:var(--body);color:var(--ink)}
.abs{position:absolute}
.center{left:0;width:1200px;text-align:center}
.accent{color:var(--blue)}
.btn{position:absolute;display:flex;align-items:center;justify-content:center;font-family:var(--body);font-weight:700;font-size:10.5px;letter-spacing:.5px;text-transform:uppercase;border-radius:4px;color:#fff;background:var(--blue)}
.btn-cyan{background:var(--cyan);color:var(--ink)}
.logo{font-family:var(--head);font-weight:700;font-size:15px;letter-spacing:1.5px;color:var(--navy);text-transform:uppercase;white-space:nowrap}

.site-nav{top:0;left:0;width:1200px;height:75px;background:#fff;border-bottom:1px solid #e8ecf4;z-index:3}
.nav-links{position:absolute;top:30px;left:504px;font-size:11px;font-weight:500;color:var(--ink)}
.nav-links span{position:absolute;white-space:nowrap}
.nav-links .active{color:var(--blue)}
.nav-links .active::after{content:"";position:absolute;left:2px;top:40px;width:12px;height:2px;background:var(--blue)}

.hero{top:75px;left:0;width:1200px;height:680px;background:linear-gradient(180deg,#eef2fe 0%,#f7f9ff 50%,#ffffff 100%)}
.badge{top:125px;left:512px;width:176px;height:25px;border-radius:4px;background:var(--cyan-soft);color:var(--blue);font-size:11.5px;font-weight:500;letter-spacing:.4px;display:flex;align-items:center;justify-content:center}
.hero-title{top:157px;font-family:var(--head);font-weight:700;font-size:38px;line-height:46px;color:var(--navy)}
.hero-sub{top:208px;font-size:15px;font-weight:500}
.hero-copy{top:240px;left:345px;width:510px;text-align:center;font-size:11px;line-height:16px;color:var(--text)}
.hero-media{top:335px;left:0;width:1200px;height:415px}

.problem-title{top:818px;font-family:var(--head);font-weight:700;font-size:37px;line-height:44px;color:var(--navy)}
.problem-copy{top:923px;left:250px;width:700px;text-align:center;font-size:11px;line-height:17px;color:var(--text)}
.laptop-area{top:975px;left:260px;width:680px;height:410px}
.laptop-media{top:1018px;left:270px;width:660px;height:360px;border-radius:14px;background:linear-gradient(180deg,#2a2d34 0%,#eceef2 22%,#f6d3d9 60%,#c5c8cf 100%)}

.practice{top:1465px;left:0;width:1200px;height:560px}
.practice-title{top:1580px;font-family:var(--head);font-weight:700;font-size:37px;line-height:44px;color:var(--navy)}
.practice-sub{top:1637px;font-size:11px;color:var(--text)}
.card{position:absolute;top:1687px;width:256px;height:235px;background:#fff;border:2px solid var(--cyan);border-radius:10px;text-align:center}
.card-icon{position:absolute;left:88px;top:29px;width:80px;height:76px;border-radius:18px;background:var(--blue);display:flex;align-items:center;justify-content:center}
.card h3{position:absolute;top:124px;left:0;width:100%;font-family:var(--head);font-weight:600;font-size:20px;color:var(--navy)}
.card p{position:absolute;top:155px;left:36px;width:184px;font-size:10.5px;line-height:15.5px;color:var(--text)}

.story-frame{top:2155px;left:172px;width:406px;height:312px;border:2.5px solid var(--blue);border-radius:6px}
.story-media{top:2123px;left:190px;width:419px;height:325px;border-radius:6px;border:1px solid #d8def0;background:linear-gradient(120deg,#f3f4f8 0%,#e7ebf6 45%,#fbeede 75%,#f2f4fa 100%)}
.story-title{top:2146px;left:653px;width:400px;font-family:var(--head);font-weight:700;font-size:33px;line-height:39px;color:var(--navy)}
.story-copy{top:2272px;left:654px;width:370px;font-size:10.5px;line-height:16.5px;color:var(--text)}

.team-kicker{top:2558px;font-size:11.5px;font-weight:500;color:var(--blue);letter-spacing:.5px}
.team-title{top:2578px;font-family:var(--head);font-weight:700;font-size:37px;line-height:44px;color:var(--navy)}
.member{position:absolute;top:2653px;width:256px;height:290px}
.member-photo{position:absolute;left:0;top:0;width:256px;height:237px;border-radius:8px;background:linear-gradient(160deg,#8d95a3 0%,#3b4352 60%,#222832 100%)}
.member-card{position:absolute;left:16px;top:194px;width:225px;height:94px;border-radius:20px;background:var(--blue);color:#fff;text-align:center}
.member-card h4{margin-top:18px;font-family:var(--head);font-weight:700;font-size:19px}
.member-card p{margin:6px auto 0;width:170px;font-size:10.5px;line-height:15px;color:#dbe6ff}

.cta-art{top:3033px;left:0;width:1200px;height:830px}
.cta-title{top:3140px;font-family:var(--head);font-weight:700;font-size:37px;line-height:43px;color:var(--navy)}
.foot-brand{top:3575px;left:190px}
.foot-about{top:3628px;left:190px;width:180px;font-size:9.5px;line-height:14px;color:#dbe3f5}
.socials{top:3682px;left:190px;display:flex;gap:6px}
.socials span{width:20px;height:20px;border-radius:50%;background:var(--blue);border:2px solid #2d63ff}
.foot-col h5{font-family:var(--head);font-weight:600;font-size:16px;color:#fff;margin-bottom:22px}
.foot-col{color:#dbe3f5;font-size:9.5px}
.foot-col li{list-style:none;height:26px;text-transform:uppercase;letter-spacing:.3px}
.contact-row{display:flex;gap:6px;align-items:flex-start;margin-bottom:13px;line-height:13px}
.news-input{width:188px;height:30px;background:#3c4f72;border-radius:2px;font-size:9.5px;color:#e3e9f5;padding:10px 14px}
.bottom-bar{top:3825px;left:0;width:1200px;height:38px;background:var(--navy-bar);font-size:10px;color:#e3e9f5}
</style>
</head>
<body>

<header class="abs site-nav">
  <div class="abs logo" style="left:190px;top:28px">Corvane Labs</div>
  <nav class="nav-links">
    <span class="active" style="left:0">HOME</span>
    <span style="left:53px">APPROACH</span>
    <span style="left:133px">PROGRAMS</span>
    <span style="left:214px">ABOUT</span>
    <span style="left:273px">CONTACT</span>
  </nav>
  <div class="btn" style="left:877px;top:22px;width:133px;height:30px">Get in touch</div>
</header>

<section class="abs hero"></section>
<div class="abs badge">LEADERSHIP TRAINING</div>
<h1 class="abs center hero-title"><span class="accent">Training</span> That Practices Back</h1>
<p class="abs center hero-sub">AI-driven sustainment that builds mastery — so you don't have to.</p>
<p class="abs hero-copy">You'll see measurable growth as your people turn insight into habit — automatically, sustainably, and without extra work for their leaders.</p>
<div class="btn" style="left:441px;top:290px;width:169px;height:36px">See how we do it</div>
<div class="btn btn-cyan" style="left:621px;top:290px;width:138px;height:36px">Get in touch</div>

<svg class="abs hero-media" viewBox="0 0 1200 415">
  <defs>
    <linearGradient id="heroPeople" x1="0" y1="0" x2="1" y2="0">
      <stop offset="0" stop-color="#e9ecf3"/>
      <stop offset=".35" stop-color="#3a3f4b"/>
      <stop offset=".7" stop-color="#f2a33a"/>
      <stop offset="1" stop-color="#dfe6f4"/>
    </linearGradient>
    <linearGradient id="heroNet" x1="0" y1="0" x2="0" y2="1">
      <stop offset="0" stop-color="#e4ebfc" stop-opacity=".2"/>
      <stop offset="1" stop-color="#c9d7f7"/>
    </linearGradient>
  </defs>
  <path d="M0 20 L1200 20 L1200 280 Q600 420 0 280 Z" fill="url(#heroNet)"/>
  <path role="img" aria-label="Three professionals — a scientist holding a molecule model, a businessman with books, and a worker with a tablet" d="M240 40 Q240 0 300 0 L900 0 Q960 0 960 40 L960 330 Q600 400 240 330 Z" fill="url(#heroPeople)" opacity=".8"/>
  <path d="M135 335 Q600 430 1065 335" fill="none" stroke="#0a4cf5" stroke-width="9" stroke-linecap="round"/>
</svg>

<h2 class="abs center problem-title">The Real Problem isn't Your People — it's<br>the <span class="accent">Forgetting Curve</span></h2>
<p class="abs problem-copy">Within a week, most training disappears. Leaders are left guessing who's using what they learned — and no one has time to fix it. We built Corvane Labs to make progress automatic, measurable, and real.</p>

<svg class="abs laptop-area" viewBox="0 0 680 410" aria-hidden="true">
  <circle cx="490" cy="125" r="95" fill="#a3efff"/>
  <circle cx="115" cy="250" r="108" fill="#b8c9ff"/>
</svg>
<div class="abs laptop-media" role="img" aria-label="Laptop showing a chart of the forgetting curve flattened by sustained practice"></div>

<svg class="abs practice" viewBox="0 0 1200 560">
  <defs>
    <linearGradient id="dots" x1="0" y1="0" x2="0" y2="1">
      <stop offset="0" stop-color="#d7e1fa" stop-opacity="0"/>
      <stop offset="1" stop-color="#c9d6f7"/>
    </linearGradient>
  </defs>
  <path d="M0 115 Q600 -60 1200 115 L1200 560 L0 560 Z" fill="#e9effd"/>
  <rect role="img" aria-label="Soft dot-matrix skyline pattern" x="0" y="180" width="1200" height="380" fill="url(#dots)"/>
</svg>
<h2 class="abs center practice-title">Practice Made <span class="accent">Permanent</span></h2>
<p class="abs center practice-sub">You'll replace "hope they remember" with a system that makes sure they do.</p>

<div class="card" style="left:190px">
  <div class="card-icon"><svg width="40" height="40" viewBox="0 0 40 40" fill="none" stroke="#fff" stroke-width="2"><path d="M12 34v-6c-4-3-6-7-5-12 2-7 9-10 15-8 6 2 9 8 7 14l3 5h-4v5h-6"/><circle cx="19" cy="17" r="4"/></svg></div>
  <h3>Learn</h3>
  <p>Fast, focused workshops, built on science, that install the mindset and skills that matter most.</p>
</div>
<div class="card" style="left:472px">
  <div class="card-icon"><svg width="40" height="40" viewBox="0 0 40 40" fill="none" stroke="#fff" stroke-width="2"><rect x="8" y="6" width="20" height="26" rx="2"/><path d="M13 13h10M13 18h10M13 23h6"/><circle cx="29" cy="27" r="5"/></svg></div>
  <h3>Certify</h3>
  <p>Programmatic AI-driven practice and feedback – mastery without management overhead.</p>
</div>
<div class="card" style="left:753px">
  <div class="card-icon"><svg width="40" height="40" viewBox="0 0 40 40" fill="none" stroke="#fff" stroke-width="2"><path d="M7 33h27M10 32v-5M16 32v-9M22 32v-13M28 32v-18M9 20l9-7 5 3 9-9"/></svg></div>
  <h3>Sustain</h3>
  <p>Light-touch challenges and dashboards that keep skills sharp long after training ends.</p>
</div>

<div class="abs story-frame"></div>
<div class="abs story-media" role="img" aria-label="Smiling businesswoman on a phone beside sketched brain and idea icons"></div>
<h2 class="abs story-title"><span class="accent">Built by People</span> Who've Led the Change Themselves</h2>
<p class="abs story-copy">Behind Corvane Labs are leaders who've lived the challenge of making learning last. They've scaled companies, built cultures, and led transformation — and now they've designed the system they always wished existed.</p>
<div class="btn" style="left:654px;top:2358px;width:151px;height:38px">Meet the team</div>

<p class="abs center team-kicker">LEADERSHIP</p>
<h2 class="abs center team-title">Meet Our <span class="accent">Team</span></h2>
<div class="member" style="left:190px">
  <div class="member-photo" role="img" aria-label="Portrait of co-founder and CEO"></div>
  <div class="member-card"><h4>Dale Hutner</h4><p>Co-Founder &amp; CEO</p></div>
</div>
<div class="member" style="left:472px">
  <div class="member-photo" role="img" aria-label="Portrait of co-founder and chief strategy officer" style="background:linear-gradient(160deg,#c79a6a 0%,#5a4634 55%,#1f1c1c 100%)"></div>
  <div class="member-card"><h4>Grant Ellery</h4><p>Co-Founder &amp; Chief Strategy Officer</p></div>
</div>
<div class="member" style="left:753px">
  <div class="member-photo" role="img" aria-label="Portrait of co-founder and chief growth officer" style="background:linear-gradient(160deg,#b08a62 0%,#5b4837 55%,#222 100%)"></div>
  <div class="member-card"><h4>Neil Brandow</h4><p>Co-Founder &amp; Chief Growth Officer</p></div>
</div>

<svg class="abs cta-art" viewBox="0 0 1200 830">
  <defs>
    <linearGradient id="ctaFill" x1="0" y1="0" x2="0" y2="1">
      <stop offset="0" stop-color="#10d6fd"/>
      <stop offset="1" stop-color="#0aaeed"/>
    </linearGradient>
  </defs>
  <rect x="0" y="0" width="1200" height="830" fill="#0d2147"/>
  <path d="M0 0 H1200 V282 Q600 510 0 282 Z" fill="url(#ctaFill)"/>
  <path d="M95 335 Q600 505 1105 335" fill="none" stroke="#0a4cf5" stroke-width="10" stroke-linecap="round"/>
</svg>
<h2 class="abs center cta-title">Ready to see what lasting<br>capability looks like?</h2>
<div class="btn" style="left:484px;top:3242px;width:231px;height:45px;font-size:11px">Start a conversation</div>

<div class="abs logo foot-brand" style="color:#fff;font-size:17px">Corvane Labs</div>
<p class="abs foot-about">Making learning that sticks through AI-driven sustainment and behavioral science.</p>
<div class="abs socials"><span></span><span></span><span></span><span></span></div>

<div class="abs foot-col" style="top:3540px;left:443px">
  <h5>Links</h5>
  <ul><li>Home</li><li>Approach</li><li>Programs</li><li>About</li><li>Contact</li></ul>
</div>
<div class="abs foot-col" style="top:3540px;left:588px">
  <h5>Get in Touch</h5>
  <div class="contact-row"><svg width="10" height="10" viewBox="0 0 10 10" fill="none" stroke="#3d7bff" stroke-width="1.2"><rect x="1" y="2" width="8" height="6"/><path d="M1 2l4 3 4-3"/></svg>contact@corvanelabs.com</div>
  <div class="contact-row"><svg width="10" height="10" viewBox="0 0 10 10" fill="#3d7bff"><path d="M2 1l2 2-1 1c1 1 2 2 3 3l1-1 2 2-1 1C5 9 1 5 1 2z"/></svg>+1 (555) 010-2840</div>
  <div class="contact-row"><svg width="10" height="12" viewBox="0 0 10 12" fill="#3d7bff"><path d="M5 0a4 4 0 014 4c0 3-4 8-4 8S1 7 1 4a4 4 0 014-4z"/></svg><span>780 Harlow Ridge Rd Suite 160<br>Alder Creek, AZ 85000</span></div>
</div>
<div class="abs foot-col" style="top:3540px;left:821px">
  <h5>Newsletter</h5>
  <div class="news-input">Email</div>
  <div class="btn" style="position:relative;margin-top:12px;width:88px;height:29px;font-size:9px">Subscribe</div>
</div>

<div class="abs bottom-bar">
  <span class="abs" style="left:190px;top:13px">© 2025 Corvane Labs. All Rights Reserved.</span>
  <span class="abs" style="left:914px;top:13px">Terms</span>
  <span class="abs" style="left:973px;top:13px">Privacy</span>
</div>

</body>
</html>
```